Awesome business card design needed

We need a new business card design to go with our new logo.
We are a web development agency that specialises in highly complex back-end integrations as opposed to design, our customers are retailers, hotels, hospitals and any other organisation that has a large online marketing department.
Take a look at our website - www.orvekplus.com for some inspiration.
We want our new business cards to exude class, professionalism and style.
We are likely to choose a high-end card to print them on but we want the design of the card itself to really turn heads.
We have no specific colour requirements, the logo as you will see is a turquoise colour R89 G171 B167 #59aba7 but it can also be in white if you want to make the colour of the card something different.
The information on the card should be:
Name
Position
Tel
email
Potentially a double sided card could have our web address, twitter and FB links.

```html
<!DOCTYPE html>
<html lang="en">
<head>
<meta charset="utf-8">
<title>Orvekplus business card</title>
<link rel="stylesheet" href="https://fonts.googleapis.com/css2?family=Roboto+Condensed:wght@700&family=Noto+Serif:wght@400&display=swap">
<style>
  :root {
    --canvas-bg: #e8e5e1;
    --card-black: #1f1f1f;
    --card-white: #ffffff;
    --teal: #59aba7;
    --teal-dark: #4e9895;
    --teal-light: #60b0ac;
    --teal-faint: #c9dedd;
    --ink: #111111;
    --icon-orange: #f0a23a;
    --icon-ring: #8a8a8a;
  }
  * { box-sizing: border-box; margin: 0; padding: 0; }
  html, body { width: 1200px; height: 1000px; overflow: hidden; }
  body { background: var(--canvas-bg); position: relative; font-family: "Noto Serif", serif; }

  .card { position: absolute; width: 694px; height: 400px; box-shadow: 0 3px 8px rgba(0,0,0,.25); overflow: hidden; }

  /* Front */
  .card-front { left: 75px; top: 100px; background: var(--card-black); }
  .accent-top { position: absolute; right: 0; top: 0; width: 232px; height: 14px; background: var(--teal); clip-path: polygon(14px 0, 100% 0, 100% 100%, 0 100%); }
  .accent-bottom { position: absolute; left: 0; bottom: 0; width: 240px; height: 15px; background: var(--teal); clip-path: polygon(0 0, 100% 0, calc(100% - 15px) 100%, 0 100%); }
  .front-wordmark { position: absolute; left: 312px; top: 146px; font-family: "Roboto Condensed", sans-serif; font-weight: 700; font-size: 78px; letter-spacing: 2px; color: #ffffff; line-height: 1; }

  /* Back */
  .card-back { left: 432px; top: 515px; background: var(--card-white); }
  .holder-name { position: absolute; left: 43px; top: 22px; font-family: "Roboto Condensed", sans-serif; font-weight: 700; font-size: 35px; color: var(--ink); line-height: 1; }
  .holder-role { position: absolute; left: 44px; top: 62px; font-family: "Roboto Condensed", sans-serif; font-weight: 700; font-size: 22px; color: var(--ink); line-height: 1; }

  .contact-list { position: absolute; left: 48px; top: 280px; list-style: none; }
  .contact-item { display: flex; align-items: center; height: 30px; font-size: 20px; color: var(--ink); }
  .contact-icon { width: 26px; height: 26px; margin-right: 10px; flex: none; }

  .watermark-name { position: absolute; left: 418px; top: 24px; height: 350px; width: 66px; writing-mode: vertical-rl; transform: rotate(180deg); font-family: "Roboto Condensed", sans-serif; font-weight: 700; font-size: 72px; letter-spacing: 3px; color: var(--teal-faint); line-height: 66px; text-align: center; }

  .social-band { position: absolute; top: 0; height: 100%; }
  .social-band--primary { left: 508px; width: 93px; background: var(--teal-dark); }
  .social-band--secondary { left: 601px; width: 93px; background: var(--teal-light); }
  .social-link { position: absolute; left: 22px; bottom: 98px; writing-mode: vertical-rl; transform: rotate(180deg); font-size: 22px; color: var(--ink); line-height: 1; white-space: nowrap; }
  .social-square { position: absolute; left: 19px; bottom: 26px; width: 48px; height: 48px; }
  .social-band--primary .social-square { background: #ffffff; }
  .social-band--secondary .social-square { background: #1f6f80; border-radius: 3px; }
</style>
</head>
<body>

<section class="card card-front" aria-label="Card front">
  <div class="accent-top"></div>
  <div class="accent-bottom"></div>
  <div class="front-wordmark">orvekplus</div>
</section>

<section class="card card-back" aria-label="Card back">
  <h1 class="holder-name">John Doe</h1>
  <p class="holder-role">Your designation</p>

  <ul class="contact-list">
    <li class="contact-item">
      <svg class="contact-icon" viewBox="0 0 26 26" aria-hidden="true">
        <circle cx="13" cy="13" r="12" fill="var(--icon-orange)" stroke="var(--icon-ring)" stroke-width="1.5"/>
        <path d="M9 7c1 0 2 2.5 1.6 3.2l-1 1c.8 1.8 2.4 3.4 4.2 4.2l1-1c.7-.4 3.2.6 3.2 1.6 0 1.2-1.4 2.2-2.6 2-4-.6-7.5-4.1-8-8C7.1 8.5 7.9 7 9 7z" fill="#5a3300"/>
      </svg>
      0198 765 432
    </li>
    <li class="contact-item">
      <svg class="contact-icon" viewBox="0 0 26 26" aria-hidden="true">
        <circle cx="13" cy="13" r="12" fill="var(--icon-orange)" stroke="var(--icon-ring)" stroke-width="1.5"/>
        <rect x="6.5" y="8.5" width="13" height="9" fill="#fff3dc" stroke="#7a4a10" stroke-width="1"/>
        <path d="M6.5 8.5l6.5 5 6.5-5" fill="none" stroke="#7a4a10" stroke-width="1"/>
      </svg>
      john@orvekplus.com
    </li>
    <li class="contact-item">
      <svg class="contact-icon" viewBox="0 0 26 26" aria-hidden="true">
        <circle cx="13" cy="13" r="12" fill="#ffffff" stroke="var(--icon-ring)" stroke-width="1.5"/>
        <circle cx="13" cy="13" r="8" fill="var(--icon-orange)" stroke="#9a5a10" stroke-width="1"/>
        <ellipse cx="13" cy="13" rx="3.5" ry="8" fill="none" stroke="#9a5a10" stroke-width="1"/>
        <path d="M5 13h16M6.5 9h13M6.5 17h13" stroke="#9a5a10" stroke-width="1"/>
      </svg>
      www.orvekplus.com
    </li>
  </ul>

  <div class="watermark-name" aria-hidden="true">orvekplus</div>

  <div class="social-band social-band--primary">
    <span class="social-link">linkhub.net/orvekplus</span>
    <span class="social-square" aria-hidden="true"></span>
  </div>
  <div class="social-band social-band--secondary">
    <span class="social-link">chirpline.net/orvekplus</span>
    <span class="social-square" aria-hidden="true"></span>
  </div>
</section>

</body>
</html>
```